Trucking company specializing in intermodal containers

We need a logo design for our trucking company based in Kent, Washington. Our companies name is Dorvale Haulworks LLC, we specialize in intermodal containers, and work off of the Crestmark rail lines and the ports. We provide service by transporting freight with our fleet of trucks. We operate within Washington, Oregon, and Idaho. Our fleet consists of an east division and a local division. Our team motto currently is globally connected, locally invested.

Target Market(s)

brokers, intermodal management companies, customers

Industry/Entity Type

Trucking Company

Contact Information for Business Card

physical address 4519 N. 163rd Pl Kent, WA 98517
office number is 253-614-9026

Font styles to use
Sans Serif

Colors

Designer to choose colors to be used in the design.

Requirements
Must have
• We need to update our current logo. Something like an emblem; that makes a statement that this logo/ sign represents Dorvale Haulworks. Something like a royal stamp but in this case a royal shield.
Nice to have
• simple, yet bold. something someone does not currently have. We need something fresh and exciting. Something that will also make a statement because currently our reputation is great within the industry and our community. But we need to reflect that we are professional and willing to provide the best service. We are open to new statement lines.
Should not have
• Should not have something thats been used before. We are open to suggestions that you have and a design that is completely unique and you make originally without what we want but what you like as well. Ofcourse it should still represent the industry we are in.

```html
<!DOCTYPE html>
<html lang="en">
<head>
<meta charset="utf-8">
<title>Dorvale Haulworks LLC – Business Card</title>
<link rel="stylesheet" href="https://fonts.googleapis.com/css2?family=Cinzel:wght@400&family=Ubuntu:wght@300;400&display=swap">
<style>
  :root {
    --page-bg: #e4e4e2;
    --card-bg: #fbfbf9;
    --brand-red: #8e2a26;
    --ink: #262626;
    --steel: #6b6b6d;
  }
  * { margin: 0; padding: 0; box-sizing: border-box; }
  html, body {
    width: 1200px; height: 800px; overflow: hidden;
    background: var(--page-bg);
  }
  .card {
    position: absolute;
    left: 100px; top: 114px;
    width: 1000px; height: 572px;
    background: var(--card-bg);
    box-shadow: 0 6px 24px rgba(0,0,0,0.12);
    font-family: "Ubuntu", sans-serif;
    font-weight: 300;
    color: var(--ink);
  }
  .brand-mark {
    position: absolute;
    left: 70px; top: 200px;
    width: 280px;
    display: flex; align-items: center; gap: 14px;
  }
  .brand-mark__dot {
    width: 26px; height: 26px; border-radius: 50%;
    background: var(--steel);
    flex: none;
  }
  .brand-mark__name {
    font-family: "Ubuntu", sans-serif;
    font-weight: 400;
    font-size: 24px;
    line-height: 1.2;
    letter-spacing: 1px;
    color: var(--brand-red);
  }
  .details {
    position: absolute;
    left: 400px; top: 60px;
    width: 540px;
  }
  .company-name {
    font-family: "Cinzel", serif;
    font-size: 30px;
    letter-spacing: 3px;
    color: var(--brand-red);
    padding-bottom: 6px;
    border-bottom: 2px solid var(--brand-red);
    display: inline-block;
  }
  .person { margin-top: 56px; letter-spacing: 6px; }
  .person__name { font-size: 40px; color: var(--brand-red); }
  .person__title { font-size: 34px; margin-left: 170px; margin-top: -4px; }
  .contact { margin-top: 40px; font-size: 27px; letter-spacing: 5px; line-height: 1.25; }
  .contact__label { color: var(--brand-red); }
  .website { margin-top: 30px; font-size: 24px; letter-spacing: 8px; color: var(--ink); }
</style>
</head>
<body>
  <main class="card">
    <div class="brand-mark">
      <span class="brand-mark__dot"></span>
      <span class="brand-mark__name">Dorvale Haulworks LLC</span>
    </div>
    <section class="details">
      <h1 class="company-name">Dorvale Haulworks LLC.</h1>
      <div class="person">
        <p class="person__name">Marcus Hale</p>
        <p class="person__title">President</p>
      </div>
      <div class="contact">
        <p class="contact__label">Physical Address</p>
        <p>4519 N. 163rd Pl Kent</p>
        <p>WA 98517</p>
        <p class="contact__label">Office number</p>
        <p>253-614-9026</p>
      </div>
      <p class="website">www.dorvalehaul.com</p>
    </section>
  </main>
</body>
</html>
```